IT Support Business needs a Flyer Designed

Have just had new logo and business cards made for new business called Orbit Logic, am now in need of a new flyer design. Orbit Logic will be providing home and small business it support.
Orbit Logic flyer design brief has been uploaded. The contest has also been changed to payment guaranteed.
If you need anymore information please feel free to contact myself.
Reason: I signed up early to take advantage of the artbazaar 24 hour sale, and was a few days late in providing a design brief. Therefore I am extending the deadline by 2 days, to ensure it lasts for a good 2 weeks.
Have worked on and refined the Design Brief a bit more, hoping it makes it a bit clearer as to what I want on the flyer. If you have any questions please do not hesitate to ask.
I have refined the design brief overnight, after receiving some feedback, please refer to newly uploaded file for this morning. I am hoping it makes things clearer and easier.
Small Business

```html
<!DOCTYPE html>
<html lang="en">
<head>
<meta charset="utf-8">
<title>Orbit Logic Flyer</title>
<link rel="stylesheet" href="https://fonts.googleapis.com/css2?family=Alegreya:ital,wght@1,400&family=Carlito:wght@400;700&display=swap">
<style>
:root{
  --bg:#e9e7e3;
  --paper:#ffffff;
  --blue:#1f5d99;
  --red:#e03a26;
  --grey-text:#6d6d6d;
  --body-text:#3a3a3a;
  --sky:#4fb3ea;
  --sky-deep:#1f6fb3;
  --steel:#8a949c;
}
*{margin:0;padding:0;box-sizing:border-box}
html,body{width:1200px;height:448px;overflow:hidden;background:var(--bg)}
body{position:relative;font-family:"Carlito","Calibri",sans-serif}
.flyer{position:absolute;width:552px;height:354px;background:var(--paper);overflow:hidden;box-shadow:0 2px 8px rgba(0,0,0,.25)}
.flyer--front{left:30px;top:26px}
.flyer--back{left:620px;top:65px}

.tagline{position:absolute;left:20px;top:22px;font-family:"Alegreya",Georgia,serif;font-style:italic;font-size:19px;line-height:18px;color:var(--grey-text)}
.brand{position:absolute;display:flex;align-items:center;gap:7px;font-weight:700;font-size:25px;color:var(--blue);letter-spacing:.2px}
.brand__dot{width:16px;height:16px;border-radius:50%;background:var(--red)}
.flyer--front .brand{left:364px;top:24px}
.flyer--back .brand{left:24px;top:264px}

.specialties-title{position:absolute;left:20px;top:66px;font-weight:700;font-size:11px;color:var(--blue)}
.service{position:absolute;top:86px;text-align:center;font-size:7.6px;line-height:9px;color:var(--body-text)}
.service__icon{display:block;position:relative;margin:0 auto 11px;width:36px;height:34px;border-radius:40%;
  background:radial-gradient(circle at 35% 30%,#ffffff 0%,var(--tone-a) 30%,var(--tone-b) 100%)}
.service__icon::after{content:"";position:absolute;left:4px;right:4px;bottom:-7px;height:5px;border-radius:50%;background:radial-gradient(ellipse,rgba(0,0,0,.22),rgba(0,0,0,0) 70%)}

.photo{position:absolute;left:0;top:174px;width:552px;height:150px;
  background:
    linear-gradient(180deg,#ffffff 0%,rgba(255,255,255,0) 22%),
    radial-gradient(ellipse 140px 60px at 300px 88px,#3c3c3c 0%,#7a7a7a 45%,rgba(150,150,150,0) 100%),
    radial-gradient(ellipse 110px 70px at 420px 40px,#5a5a5a 0%,rgba(120,120,120,0) 100%),
    linear-gradient(100deg,#f2f2f2 0%,#cfcfcf 35%,#a9a9a9 60%,#dcdcdc 85%,#f4f4f4 100%)}
.band{position:absolute;left:0;bottom:0;width:552px}
.band-copy{position:absolute;left:20px;top:307px;font-size:10.3px;line-height:13.5px;color:#fff}

.lead{position:absolute;left:24px;top:16px;width:510px;font-weight:700;font-size:12.9px;line-height:16.5px;color:var(--blue)}
.device{position:absolute;border-radius:4px;background:linear-gradient(160deg,var(--tone-a),var(--tone-b))}
.device::after{content:"";position:absolute;left:6%;right:6%;bottom:-6px;height:5px;border-radius:50%;background:radial-gradient(ellipse,rgba(0,0,0,.2),rgba(0,0,0,0) 70%)}
.pricing{position:absolute;left:24px;top:180px;width:410px;font-weight:700;font-size:14.2px;line-height:17.5px;color:var(--red)}
.callout{position:absolute;right:22px;top:234px;text-align:right;font-family:"Alegreya",Georgia,serif;font-style:italic;font-size:15.5px;line-height:16.5px;color:var(--grey-text)}
.callout strong{font-family:"Carlito",sans-serif;font-style:normal;font-weight:700;color:var(--red)}
.contact{position:absolute;color:#fff;font-size:9.8px;line-height:13px;display:flex;flex-direction:column}
.contact span{display:flex;align-items:center;gap:3px}
.contact--biz{left:174px;top:320px}
.contact--phone{left:290px;top:323px;font-size:13px}
.contact--web{right:22px;top:320px;align-items:flex-end}
.contact svg{fill:#fff}
</style>
</head>
<body>

<section class="flyer flyer--front">
  <p class="tagline">Providing solutions for all your<br>computer and technical equipment needs.</p>
  <div class="brand"><span class="brand__dot"></span>Orbit Logic</div>
  <h2 class="specialties-title">Orbit Logic specialises in:</h2>

  <div class="service" style="left:14px;width:72px"><span class="service__icon" style="--tone-a:var(--sky);--tone-b:var(--sky-deep)" role="img" aria-label="Computer repair icon"></span>Computer repair, service installation and upgrades</div>
  <div class="service" style="left:90px;width:66px"><span class="service__icon" style="--tone-a:#b9c6d2;--tone-b:#4f6f92" role="img" aria-label="Home network icon"></span>Support to set up and secure your home network</div>
  <div class="service" style="left:166px;width:72px"><span class="service__icon" style="--tone-a:#8bbf5a;--tone-b:#3b2f2a" role="img" aria-label="Operating system icon"></span>Sharing the tricks and tips to manage your new operating system</div>
  <div class="service" style="left:244px;width:60px"><span class="service__icon" style="--tone-a:var(--sky);--tone-b:var(--sky-deep)" role="img" aria-label="Software install icon"></span>Assistance in installing and configuring new software</div>
  <div class="service" style="left:311px;width:112px"><span class="service__icon" style="--tone-a:#cfe3f3;--tone-b:#6ea8d6" role="img" aria-label="Online connection icon"></span>Getting you connected online and across social media faster, including Internet, email, video calls, social pages etc</div>
  <div class="service" style="left:426px;width:56px"><span class="service__icon" style="--tone-a:var(--sky);--tone-b:#1b5f9c" role="img" aria-label="Data backup icon"></span>Data backup and recovery</div>
  <div class="service" style="left:482px;width:56px"><span class="service__icon" style="--tone-a:#9fd3f2;--tone-b:#2d86c7" role="img" aria-label="Tuition icon"></span>Tuition in programs and technology</div>

  <div class="photo" role="img" aria-label="Black and white photo of a hand typing on a keyboard"></div>

  <svg class="band" width="552" height="84" viewBox="0 0 552 84" aria-hidden="true">
    <path d="M0 4 C180 -4 380 10 552 74 L552 84 L0 84Z" fill="var(--red)"/>
    <path d="M0 12 C190 4 390 20 552 80 L552 84 L0 84Z" fill="var(--blue)"/>
  </svg>
  <p class="band-copy">With over 15 years experience in the IT sector, Daniel from<br>Orbit Logic provides friendly, reliable and professional service,<br>supporting you to build your skills and knowledge to maximise your IT requirements.</p>
</section>

<section class="flyer flyer--back">
  <p class="lead">Our services and expertise extends across PC’s, Laptops, printers, scanners, routers, tablet, mobile phone, cameras, television and arcade consoles, with the ability to work onsite or remotely as required.</p>

  <div class="device" style="left:20px;top:84px;width:94px;height:62px;--tone-a:#7fd0f5;--tone-b:#2a84c4" role="img" aria-label="Desktop computer with tower and keyboard"></div>
  <div class="device" style="left:124px;top:92px;width:78px;height:50px;--tone-a:#3f8fd0;--tone-b:#0f2a44" role="img" aria-label="Flat screen monitor"></div>
  <div class="device" style="left:216px;top:84px;width:68px;height:62px;--tone-a:#ffffff;--tone-b:#a9b0b6" role="img" aria-label="Printer"></div>
  <div class="device" style="left:296px;top:88px;width:76px;height:54px;--tone-a:#f4f6f7;--tone-b:#b7bec4" role="img" aria-label="Scanner"></div>
  <div class="device" style="left:388px;top:94px;width:48px;height:48px;--tone-a:#7ac143;--tone-b:#2b2b2b" role="img" aria-label="Tablet and phone"></div>
  <div class="device" style="left:450px;top:82px;width:70px;height:64px;--tone-a:#e6e9ec;--tone-b:#5c6770" role="img" aria-label="Webcam and router"></div>

  <p class="pricing">Orbit Logic service fees start at $40 per hour however packages and flexible pricing for more complex tasks are available.</p>
  <div class="device" style="left:448px;top:166px;width:72px;height:54px;--tone-a:#8fd6f7;--tone-b:#2578b8" role="img" aria-label="Laptop"></div>

  <p class="callout">With no call out fee, talk to <strong>Daniel</strong> today<br>to solve your IT and technology challenges.</p>

  <div class="brand"><span class="brand__dot"></span>Orbit Logic</div>

  <svg class="band" width="552" height="70" viewBox="0 0 552 70" aria-hidden="true">
    <path d="M0 66 C140 26 360 8 552 4 L552 70 L0 70Z" fill="var(--red)"/>
    <path d="M0 70 C150 34 370 18 552 14 L552 70Z" fill="var(--blue)"/>
  </svg>

  <div class="contact contact--biz">
    <span>ABN is 48 120 765 309</span>
    <span><svg width="7" height="9" viewBox="0 0 10 14"><path d="M5 0a5 5 0 0 0-5 5c0 4 5 9 5 9s5-5 5-9a5 5 0 0 0-5-5zm0 7a2 2 0 1 1 0-4 2 2 0 0 1 0 4z"/></svg>Riverton, Victoria</span>
  </div>
  <div class="contact contact--phone">
    <span><svg width="10" height="10" viewBox="0 0 16 16"><path d="M3 1l3 3-2 2c1 2 3 4 5 5l2-2 3 3-2 3C6 15 1 10 1 3z"/></svg>0400 123 987</span>
  </div>
  <div class="contact contact--web">
    <span><svg width="9" height="7" viewBox="0 0 14 10"><path d="M0 0h14v10H0z M1 1l6 5 6-5" fill="none" stroke="#fff" stroke-width="1.4"/></svg>hello@orbitlogic.com.au</span>
    <span><svg width="8" height="8" viewBox="0 0 10 10"><circle cx="5" cy="5" r="4.3" fill="none" stroke="#fff" stroke-width="1.2"/><path d="M1 5h8M5 1c-2 2-2 6 0 8M5 1c2 2 2 6 0 8" fill="none" stroke="#fff" stroke-width=".9"/></svg>www.orbitlogic.com.au</span>
  </div>
</section>

</body>
</html>
```